Letterhead design for Dental Practice - Ashby Lane Dental Care

Letterhead for Private Dental Practice. To be used for all official correspondance and for printing treatment details on to be given to patients.

Target Market(s)

Private dental patients

Industry/Entity Type

Dental Clinic

Font styles to use
Other font styles liked:
• nexa-light

Colors
33a6d7
1c66ac
85abd2

Requirements
Must have
• info in the footer and header needs to be 3.5cm from upper/lower boader of paper, see photo in uploaded files
• info details:
• tel. 01604 947 305
• email info@ashbylanedc.co.uk
• ashbylanedentalcare.co.uk
• 17b Ashby Lane Kingsthorpe Northampton NN2 6QT
• nexa-light font as in uploaded logo files
Should not have
• No funny tooth pictures

```html
<!DOCTYPE html>
<html lang="en">
<head>
<meta charset="utf-8">
<title>Ashby Lane Dental Care – Stationery</title>
<link rel="stylesheet" href="https://fonts.googleapis.com/css2?family=Questrial&display=swap">
<style>
  :root {
    --brand-blue: #33a6d7;
    --brand-navy: #1c66ac;
    --brand-soft: #85abd2;
    --ink: #3d3d3d;
    --ink-muted: #9a9a9a;
    --rule: #2b2b2b;
    --paper: #ffffff;
    --folder-top: #f1f1f1;
    --folder-bottom: #e6e6e6;
    --backdrop: #e9e9e9;
  }
  * { box-sizing: border-box; margin: 0; padding: 0; }
  html, body {
    width: 1200px; height: 894px; overflow: hidden;
    background: var(--backdrop);
    font-family: "Questrial", "Century Gothic", sans-serif;
    color: var(--ink);
  }
  .canvas { position: relative; width: 1200px; height: 894px; }

  /* Letterhead */
  .letterhead {
    position: absolute; left: 74px; top: 73px; width: 521px; height: 675px;
    background: var(--paper); overflow: hidden;
  }
  .letterhead__header {
    position: absolute; left: 46px; right: 46px; top: 50px; height: 26px;
    display: flex; align-items: flex-end; gap: 8px;
  }
  .letterhead__header .rule { flex: 1; height: 1px; background: var(--rule); margin-bottom: 2px; }
  .brand-name {
    font-size: 15px; color: var(--brand-blue); white-space: nowrap; letter-spacing: 0.2px;
    line-height: 1;
  }
  .brand-dot {
    display: inline-block; width: 8px; height: 8px; border-radius: 50%;
    background: var(--brand-blue); margin-right: 6px; vertical-align: 1px;
  }
  .letterhead__body {
    position: absolute; left: 55px; width: 411px; top: 114px;
    font-size: 10.4px; line-height: 17.1px; text-align: justify; hyphens: auto;
  }
  .letterhead__body p + p { margin-top: 17.1px; }
  .letterhead__watermark {
    position: absolute; left: 0; right: 0; top: 340px; text-align: center;
    font-size: 38px; color: var(--brand-blue); opacity: 0.06; white-space: nowrap;
  }
  .sign-off {
    position: absolute; left: 57px; right: 55px; top: 541px;
    display: flex; justify-content: space-between; align-items: flex-start;
  }
  .sign-off .brand-name { color: var(--ink-muted); font-size: 13px; margin-top: 15px; }
  .sign-off .brand-dot { background: var(--ink-muted); }
  .signatory__name { font-size: 14.5px; color: var(--ink); }
  .signatory__role { font-size: 9.5px; margin-top: 7px; }
  .letterhead__footer-rule {
    position: absolute; left: 46px; right: 46px; top: 608px; height: 1px; background: var(--rule);
  }
  .contact {
    position: absolute; left: 54px; top: 619px; font-size: 7.2px; color: #555; line-height: 12px;
  }
  .contact__row { display: flex; align-items: center; gap: 5px; }
  .contact__row svg { width: 8px; height: 8px; }
  .address {
    position: absolute; right: 55px; top: 620px; text-align: right; line-height: 12px;
  }
  .address__street { font-size: 6.6px; color: var(--brand-blue); font-weight: bold; }
  .address__web { font-size: 8px; color: #333; letter-spacing: 0.4px; }

  /* Folder cover */
  .folder {
    position: absolute; left: 638px; top: 72px; width: 498px; height: 676px;
    border-radius: 14px; overflow: hidden;
    background: linear-gradient(180deg, var(--folder-top), var(--folder-bottom));
  }
  .folder__decor {
    position: absolute; left: 320px; top: 440px; width: 190px; height: 190px;
    border-radius: 50%; border: 14px solid var(--brand-soft); opacity: 0.2;
  }
  .folder__brand {
    position: absolute; left: 0; right: 0; top: 580px; text-align: center;
  }
  .folder__brand .brand-name { font-size: 29px; }
  .folder__brand .brand-dot { width: 16px; height: 16px; vertical-align: 3px; margin-right: 10px; }
</style>
</head>
<body>
<main class="canvas">

  <section class="letterhead" aria-label="Letterhead">
    <header class="letterhead__header">
      <span class="rule"></span>
      <span class="brand-name"><span class="brand-dot"></span>Ashby Lane Dental Care</span>
      <span class="rule"></span>
    </header>

    <div class="letterhead__watermark" aria-hidden="true">Ashby Lane Dental Care</div>

    <div class="letterhead__body">
      <p>Lorem ipsum dolor sit amet, consectetur adipiscing elit. Donec orci purus, luctus vitae dignissim eu, iaculis sed purus. Vivamus faucibus, ipsum nec aliquet viverra, leo mauris condimentum ligula, sit amet sagittis enim ligula quis arcu. Nam egestas tortor id nisi porttitor mattis. In tortor ante, ultricies in suscipit a, tempus non massa. Vivamus et auctor mi. Fusce vel massa nulla. Phasellus nec eros mauris, et scelerisque orci. Donec malesuada orci vitae nulla accumsan porta a id massa.</p>
      <p>Quisque accumsan iaculis magna sit amet fringilla. Maecenas consequat, magna eget tincidunt semper, odio nibh rutrum mi, id feugiat ante nisi eu risus. Vestibulum nunc orci, rhoncus a placerat in, ultricies in mi. Cras mattis varius eros, vel fringilla nisi suscipit eget. Quisque scelerisque sagittis nulla at porttitor. Mauris a justo et tellus interdum tristique. Sed id augue vitae urna euismod commodo aliquet a quam. Pellentesque arcu velit, cursus et malesuada ut, consequat et diam. Nullam erat sem, rhoncus id ullamcorper vitae, rhoncus et arcu. In ultricies ultricies nulla.</p>
      <p>Kut rutrum nisi iaculis at. Donec eu magna a metus ornare faucibus. Fusce aliquet faucibus ultricies. Morbi semper, est id tincidunt gravida, sem arcu adipiscing lacus, ac bibendum nulla leo eu purus. Quisque nec diam sed risus consectetur a ccumsan quis quis nibh. Vestibulum id purus lorem. Donec eu magna a metus ornare faucibus. Fusce aliquet faucibus ultricies. Morbi semper, est id tincidunt gravida, sem arcu adipiscing lacus, ac bibendum nulla leo eu purus. Quisque nec diam sed risus consectetur a ccumsan quis quis nibh. Vestibulum id purus lorem.</p>
    </div>

    <div class="sign-off">
      <span class="brand-name"><span class="brand-dot"></span>Ashby Lane Dental Care</span>
      <div class="signatory">
        <div class="signatory__name">Clara Hensley</div>
        <div class="signatory__role">Co-Founder &amp; CEO</div>
      </div>
    </div>

    <div class="letterhead__footer-rule"></div>

    <div class="contact">
      <div class="contact__row">
        <svg viewBox="0 0 10 10" aria-hidden="true"><circle cx="5" cy="5" r="5" fill="#33a6d7"/><path d="M3 3.2c.3-.4.8-.4 1 0l.3.6c.1.3 0 .5-.2.6.3.6.7 1 1.3 1.3.1-.2.3-.3.6-.2l.6.3c.4.2.4.7 0 1-.6.5-1.5.3-2.5-.6S2.5 3.8 3 3.2z" fill="#fff"/></svg>
        <span>01604 947 305</span>
      </div>
      <div class="contact__row">
        <svg viewBox="0 0 10 10" aria-hidden="true"><circle cx="5" cy="5" r="5" fill="#33a6d7"/><rect x="2.6" y="3.3" width="4.8" height="3.4" fill="none" stroke="#fff" stroke-width=".7"/><path d="M2.6 3.3 5 5.3l2.4-2" fill="none" stroke="#fff" stroke-width=".7"/></svg>
        <span>info@ashbylanedc.co.uk</span>
      </div>
    </div>

    <div class="address">
      <div class="address__street">17b Ashby Lane Kingsthorpe Northampton NN2 6QT</div>
      <div class="address__web">www.ashbylanedentalcare.co.uk</div>
    </div>
  </section>

  <section class="folder" aria-label="Presentation folder cover">
    <div class="folder__decor" aria-hidden="true"></div>
    <div class="folder__brand">
      <span class="brand-name"><span class="brand-dot"></span>Ashby Lane Dental Care</span>
    </div>
  </section>

</main>
</body>
</html>
```